Business Cards for Branding (Advertising) Agency

We need stylish and cool business cards.
Additional info:
1) Logo - see the attachment. You can use either the three penguins or just one penguin face (square or round) - at your discretion.
2) Text and other stuff for business card:
front side:
-Logo and company name: company name - Northern Herons - should be in English as is in logo. This is the only exception. The rest of the text will be in Russian.
-Who we are: Брендинговое агентство
-First and last name:
-Position: Управляющий партнёр
-Address:
-Phone:
-Email:
-Website:
Note: please don't use names of information fields, such as: who we are, first and last name, position, address, phone, email and website.

3) Our suggestions on design:
-The backside of the business card can be either blank or has something on it - at your discretion.
-The business card background should be either white or grey (you can use any tone of grey).

Additional Information:
1) БРЕНДИНГОВОЕ АГЕНТСТВО
2) ул. Верескова - these two words should be together on the same line
3) тел.: +7 (495) 381-60-92
моб.: +7 (916) 507-28-14

Reason: We would like to receive more stylish designs.

```html
<!DOCTYPE html>
<html lang="ru">
<head>
<meta charset="utf-8">
<title>Northern Herons — визитная карточка</title>
<link rel="stylesheet" href="https://fonts.googleapis.com/css2?family=PT+Serif&family=Arimo&display=swap">
<style>
  :root {
    --stage: #000000;
    --card: #ffffff;
    --ink: #1a1a1a;
    --ink-soft: #2b2b2b;
    --wedge-light: #e4e4e4;
    --wedge-dark: #c9c9c9;
    --label: #ffffff;
  }
  html, body {
    margin: 0;
    width: 1200px;
    height: 900px;
    overflow: hidden;
    background: var(--stage);
  }
  .stage {
    position: relative;
    width: 1200px;
    height: 900px;
  }
  .card {
    position: absolute;
    left: 26px;
    top: 53px;
    width: 1016px;
    height: 607px;
    background: var(--card);
    overflow: hidden;
  }
  .card__wedge {
    position: absolute;
    inset: 0;
  }
  .identity {
    position: absolute;
    left: 62px;
    top: 126px;
    width: 450px;
    text-align: center;
    font-family: "PT Serif", Georgia, serif;
    font-size: 30px;
    color: var(--ink);
    line-height: 1;
  }
  .identity p { margin: 0 0 46px; }
  .contacts {
    position: absolute;
    left: 56px;
    top: 486px;
    font-family: "Arimo", Arial, sans-serif;
    font-size: 19.5px;
    color: var(--ink);
    line-height: 1.3;
  }
  .contacts p { margin: 0; }
  .contacts .address { margin-bottom: 6px; }
  .brand {
    position: absolute;
    left: 596px;
    top: 250px;
    width: 400px;
    text-align: center;
  }
  .brand__mark {
    display: block;
    width: 64px;
    height: 64px;
    margin: 0 auto 18px;
    border-radius: 50%;
    background: var(--ink);
  }
  .brand__name {
    margin: 0;
    font-family: "PT Serif", Georgia, serif;
    font-size: 46px;
    color: var(--ink);
    line-height: 1;
  }
  .brand__site {
    margin: 14px 0 0;
    font-family: "Arimo", Arial, sans-serif;
    font-size: 19.5px;
    color: var(--ink-soft);
  }
  .side-label {
    position: absolute;
    left: 132px;
    top: 718px;
  }
  .side-label__text {
    position: absolute;
    left: 324px;
    top: 30px;
    margin: 0;
    font-family: "PT Serif", Georgia, serif;
    font-size: 50px;
    color: var(--label);
    white-space: nowrap;
  }
</style>
</head>
<body>
<main class="stage">
  <section class="card">
    <svg class="card__wedge" width="1016" height="607" viewBox="0 0 1016 607" role="img" aria-label="Rising diagonal striped band in light grey">
      <defs>
        <linearGradient id="wedgeFill" x1="0" y1="1" x2="1" y2="0">
          <stop offset="0" stop-color="var(--wedge-light)"/>
          <stop offset="1" stop-color="var(--wedge-dark)"/>
        </linearGradient>
      </defs>
      <polygon points="10,567 1004,312 1004,595 10,595" fill="url(#wedgeFill)"/>
    </svg>

    <div class="identity">
      <p class="identity__role">Брендинговое агентство</p>
      <p class="identity__name">Марина Ольховская</p>
      <p class="identity__title">Управляющий партнёр</p>
    </div>

    <div class="brand">
      <span class="brand__mark"></span>
      <p class="brand__name">Northern Herons</p>
      <p class="brand__site">www.northernherons.ru</p>
    </div>

    <div class="contacts">
      <p class="address">119071, г. Москва, ул. Верескова, д.21, стр.4</p>
      <p class="phone">+7 (916) 507-28-14</p>
      <p class="email">marina@northernherons.ru</p>
    </div>
  </section>

  <div class="side-label">
    <svg width="310" height="90" viewBox="0 0 310 90" aria-hidden="true">
      <path d="M300 48 C 240 92, 90 90, 8 12" fill="none" stroke="var(--label)" stroke-width="5" stroke-linecap="round"/>
      <path d="M2 4 L 26 14 M2 4 L 6 30" fill="none" stroke="var(--label)" stroke-width="5" stroke-linecap="round"/>
    </svg>
    <p class="side-label__text">front side</p>
  </div>
</main>
</body>
</html>
```